professional business card design

Business card design. Photos have been uploaded and i am open to the designer choosing which photos to use. Would like the card to be mostyly in a grey scale design with black, whites, silver & grey colours. I have added copy of our flyer as would like on the back side of card our services to be listed. Do not use any bright colurs such as blue red green or yellow. i need to be able to edit the phone number and naem in the final card design submitted.

Target Market(s)

Clients

Industry/Entity Type

earhmovibng and transport

Contact Information for Business Card

Director Name, address, email, phone number and services

Colors

Designer to choose only greyscale colors for use in the design.

Requirements
Should not have
• no yellow, red, blue or green

```html
<!DOCTYPE html>
<html lang="en">
<head>
<meta charset="utf-8">
<title>RHX Pty Ltd – Business Card</title>
<link href="https://fonts.googleapis.com/css2?family=Montserrat:wght@400;500;600;700;800&display=swap" rel="stylesheet">
<style>
  :root{
    --page:#ececec;
    --ink:#141416;
    --black:#0b0b0c;
    --charcoal:#2a2a2c;
    --steel:#4a4a4d;
    --silver:#bdbdbd;
    --silver-light:#d4d4d4;
    --white:#ffffff;
  }
  *{margin:0;padding:0;box-sizing:border-box}
  html,body{width:1005px;height:1200px;overflow:hidden;background:var(--page);font-family:"Montserrat",sans-serif}
  .card{position:absolute;left:112px;width:780px;height:463px;overflow:hidden;box-shadow:4px 6px 10px rgba(0,0,0,.35)}
  .card--front{top:90px;background:radial-gradient(ellipse at 50% 20%,#4a4a4c 0%,#1f1f21 45%,#0c0c0d 100%)}
  .card--back{top:645px;background:linear-gradient(180deg,#c9c9c9 0%,#bcbcbc 100%)}

  /* front */
  .brand{position:absolute;top:62px;left:0;width:100%;text-align:center;color:var(--silver-light)}
  .brand__name{font-size:74px;font-weight:800;letter-spacing:6px;line-height:1}
  .brand__suffix{font-size:18px;font-weight:700;margin-top:6px}
  .front-photo{position:absolute;left:0;top:190px;width:100%;height:168px;
    background:
      linear-gradient(90deg,rgba(0,0,0,.35) 0%,rgba(0,0,0,0) 30%,rgba(0,0,0,0) 70%,rgba(0,0,0,.3) 100%),
      linear-gradient(180deg,#2c2c2e 0%,#1a1a1b 45%,#3c3c3e 75%,#555557 100%)}
  .contact-band{position:absolute;left:0;top:358px;width:100%;height:90px;background:linear-gradient(180deg,#d6d6d6 0%,#c2c2c2 100%)}
  .base-strip{position:absolute;left:0;bottom:0;width:100%;height:15px;background:var(--black)}
  .person{position:absolute;right:52px;top:316px;text-align:right}
  .person__role{position:absolute;right:0;top:-8px;font-size:11px;font-weight:500;color:#a8a8a8}
  .person__name{font-size:28px;font-weight:600;line-height:34px;color:var(--white);text-shadow:0 1px 3px rgba(0,0,0,.6)}
  .contacts{position:absolute;top:373px;left:56px;width:690px;display:grid;grid-template-columns:390px 300px;row-gap:10px}
  .contact{display:flex;align-items:center;gap:14px;font-size:19px;line-height:24px;font-weight:500;color:var(--ink)}
  .contact svg{width:16px;height:16px;flex:none;fill:var(--ink)}

  /* back */
  .services-bar{position:absolute;top:12px;left:0;width:100%;height:30px;background:var(--black);color:var(--white);text-align:center;font-size:19px;font-weight:700;line-height:30px;letter-spacing:.5px}
  .services{position:absolute;top:68px;display:flex;flex-direction:column;gap:7px;list-style:none}
  .services--left{left:110px}
  .services--right{left:465px}
  .services li{position:relative;padding-left:16px;font-size:13.5px;font-weight:600;color:var(--ink);line-height:16.5px}
  .services li::before{content:"";position:absolute;left:0;top:6px;width:5px;height:5px;border-radius:50%;background:var(--ink)}
  .back-photo{position:absolute;left:0;top:222px;width:100%;height:241px;
    background:
      radial-gradient(ellipse 22% 60% at 22% 62%,rgba(240,240,240,.85) 0%,rgba(240,240,240,0) 100%),
      radial-gradient(ellipse 20% 60% at 74% 62%,rgba(235,235,235,.85) 0%,rgba(235,235,235,0) 100%),
      radial-gradient(ellipse 16% 45% at 52% 55%,rgba(40,40,42,.8) 0%,rgba(40,40,42,0) 100%),
      radial-gradient(ellipse 14% 50% at 5% 60%,rgba(30,30,32,.7) 0%,rgba(30,30,32,0) 100%),
      linear-gradient(180deg,#bcbcbc 0%,#9a9a9a 45%,#6e6e70 80%,#b4b4b4 100%)}
</style>
</head>
<body>

<section class="card card--front" aria-label="Business card front">
  <div class="brand">
    <div class="brand__name">RHX</div>
    <div class="brand__suffix">Pty Ltd</div>
  </div>
  <div class="front-photo" role="img" aria-label="Photo of a road train truck hauling three tipper trailers on a dirt yard"></div>
  <div class="contact-band"></div>
  <div class="person">
    <span class="person__role">Director</span>
    <div class="person__name">Example Name</div>
  </div>
  <div class="contacts">
    <div class="contact">
      <svg viewBox="0 0 16 16"><path d="M8 0a5.5 5.5 0 0 0-5.5 5.5C2.5 9.6 8 16 8 16s5.5-6.4 5.5-10.5A5.5 5.5 0 0 0 8 0zm0 7.6a2.1 2.1 0 1 1 0-4.2 2.1 2.1 0 0 1 0 4.2z"/></svg>
      <span>Example Of Youre Addess</span>
    </div>
    <div class="contact">
      <svg viewBox="0 0 16 16"><path d="M1 3h14v10H1zM2.2 4.2 8 8.6l5.8-4.4z" fill-rule="evenodd"/></svg>
      <span>office@rhxhaul.com</span>
    </div>
    <div class="contact">
      <svg viewBox="0 0 16 16"><path d="M3.6 1 6 3.4 4.6 5.6a9 9 0 0 0 5.8 5.8L12.6 10 15 12.4 13 15C6.6 14.6 1.4 9.4 1 3z"/></svg>
      <span>300 555 0142</span>
    </div>
    <div class="contact">
      <svg viewBox="0 0 16 16"><path d="M8 0a8 8 0 1 0 0 16A8 8 0 0 0 8 0zm5.9 7h-2.5a12 12 0 0 0-1-4.6A6 6 0 0 1 13.9 7zM8 2c.7.8 1.3 2.6 1.4 5H6.6C6.7 4.6 7.3 2.8 8 2zM5.6 2.4a12 12 0 0 0-1 4.6H2.1a6 6 0 0 1 3.5-4.6zM2.1 9h2.5a12 12 0 0 0 1 4.6A6 6 0 0 1 2.1 9zM8 14c-.7-.8-1.3-2.6-1.4-5h2.8c-.1 2.4-.7 4.2-1.4 5zm2.4-.4a12 12 0 0 0 1-4.6h2.5a6 6 0 0 1-3.5 4.6z"/></svg>
      <span>rhxhaul.com</span>
    </div>
  </div>
  <div class="base-strip"></div>
</section>

<section class="card card--back" aria-label="Business card back">
  <div class="services-bar">OUR SERVICES</div>
  <ul class="services services--left">
    <li>Over size loads / Hot Shot Loads</li>
    <li>Heavy Vehicle Recovery Services</li>
    <li>Potable Water Deliveries</li>
    <li>Road Building / Maintenance</li>
    <li>Earthworks</li>
    <li>Sand &amp; Metal Supply &amp; Cartage</li>
  </ul>
  <ul class="services services--right">
    <li>Road Train Tippers</li>
    <li>Road Train Tankers</li>
    <li>Road Train Flat Tops</li>
    <li>Drop Deck Trailers</li>
    <li>Mine Site accredited<br>equipment &amp; Operators</li>
  </ul>
  <div class="back-photo" role="img" aria-label="Photo of a row of prime mover trucks, one carrying an oversize grader on a low loader"></div>
</section>

</body>
</html>
```